Powerpoint template for basic scientists studying immunology

We are an QVA-funded consortium of basic science researchers at academic centers in Boston, Philadelphia and Oxford, UK. We study why the immune system fails to get rid of Hepatitis C virus, and whether new antiviral treatments that reduce viral load improve immune function. We are looking for a powerpoint template that we can use as a "brand" for our research consortium. It would feature a logo (file attached) and should represent the fonts/colors contained in the logo. We we would present at meetings and to program officers at the QVA, but, if we ever get around to it, would also be on a website.

The scientific description is as follows:
Hepatitis C virus (HCV) infects 185 million persons worldwide, is the leading indication for liver transplantation and, in the US, has a higher mortaliy rate than HIV. The annual healthcare costs associated with HCV exceed $9 billion, a number expected to increase as the epidemic matures and end stage liver disease peaks over the next decade. By virtue of its remarkable predilection for persistence, HCV is a model chronic viral infection. Mounting evidence supports the idea that HCV, while inducing type I IFN expression, maintains chronicity by virtue of global suppression of host innate and adaptive immunity. The mainstay of treatment for the last two decades, IFN-α-based regimens are ineffective in many patient subgroups and have significant side effects. The recent development of highly effective direct acting antivirals (DAA) against HCV promises to alter the landscape of this devastating infection by offering curative therapy without IFN. However, it remains essential that we understand what type of immunity remains following pharmacological eradication of the virus because: a) many HCV infected subjects remain at risk for re-infection; and b) DAAs are only partially effective in some patient subgroups, particularly those with past treatment with IFN. The imminent availability of IFN-free treatment for HCV offers an unprecedented opportunity to understand broad questions about alterations in immunity in humans with cure of chronic infections. Until now, mechanistic dissection of human immune responses has been challenging due to limited ability to directly perturb the system. The organizing principle of this U19 Program therefore, is to capitalize on the unique opportunity to, for the first time, cure chronic viral infection in humans without immune modulation and interrogate the immunological changes that ensue. Thus, we have formulated the following central hypothesis for this Program: DAA-mediated cure of chronic HCV infection will lead to partial "resetting" of some immune abnormalities, but specific immunological defects will persist in some subjects that prevent development of optimal immunity to HCV. We will test this hypothesis through a set of integrated Projects and Cores.

Target Market(s)

scientists.

Industry/Entity Type

Biotechnology

Font styles to use
Sans Serif

Requirements
Must have
• Very clean, very simple. Mostly whitespace for puting graphs and data on. Colors, fonts should match the logo. Please see ppt example.
Should not have
• too much of the ppt covered with the logo.

```html
<!DOCTYPE html>
<html lang="en">
<head>
<meta charset="utf-8">
<title>Project Slide</title>
<link href="https://fonts.googleapis.com/css2?family=Roboto+Condensed:wght@400;500&display=swap" rel="stylesheet">
<style>
  :root {
    --brand-blue: #0098c9;
    --heading-blue: #2b8db4;
    --body-grey: #5a5a5a;
    --white: #ffffff;
  }
  * { box-sizing: border-box; margin: 0; padding: 0; }
  html, body {
    width: 1200px;
    height: 900px;
    overflow: hidden;
    background: var(--white);
    font-family: "Roboto Condensed", "Arial Narrow", sans-serif;
  }
  .slide {
    position: relative;
    width: 1200px;
    height: 900px;
    background: var(--white);
  }
  .slide-header {
    position: absolute;
    top: 0; left: 0;
    width: 1200px;
    height: 95px;
    background: var(--brand-blue);
    display: flex;
    align-items: center;
    justify-content: space-between;
    padding: 0 26px 0 25px;
  }
  .slide-title {
    color: var(--white);
    font-weight: 400;
    font-size: 46px;
    letter-spacing: 0;
    line-height: 1;
    padding-bottom: 2px;
  }
  .consortium-name {
    display: flex;
    align-items: center;
    gap: 10px;
    color: var(--white);
    font-size: 22px;
    font-weight: 400;
  }
  .consortium-dot {
    width: 14px; height: 14px;
    border-radius: 50%;
    background: var(--white);
  }
  .topic-list {
    position: absolute;
    top: 176px;
    left: 58px;
    list-style: none;
  }
  .topic {
    position: relative;
    padding-left: 47px;
    margin-bottom: 94px;
  }
  .topic-bullet {
    position: absolute;
    left: 0;
    top: 9px;
    width: 24px;
    height: 24px;
  }
  .topic-title {
    color: var(--heading-blue);
    font-size: 29px;
    font-weight: 400;
    line-height: 40px;
  }
  .topic-body {
    color: var(--body-grey);
    font-size: 22.5px;
    line-height: 36px;
  }
  .topic-body span { display: block; white-space: nowrap; }
</style>
</head>
<body>
<main class="slide">
  <header class="slide-header">
    <h1 class="slide-title">PROJECT TITLE HERE</h1>
    <div class="consortium-name"><span class="consortium-dot"></span>Helix Consortium</div>
  </header>

  <ul class="topic-list">
    <li class="topic">
      <svg class="topic-bullet" viewBox="0 0 24 24" aria-hidden="true"><circle cx="12" cy="12" r="8" fill="none" stroke="var(--brand-blue)" stroke-width="5"/></svg>
      <h2 class="topic-title">Subtext title here</h2>
      <p class="topic-body"><span>Subtext here Subtext here Subtext here Subtext here Subtext here Subtext here Subtext here Subtext here</span><span>Subtext here Subtext here Subtext here Subtext here Subtext here Subtext here</span></p>
    </li>
    <li class="topic">
      <svg class="topic-bullet" viewBox="0 0 24 24" aria-hidden="true"><circle cx="12" cy="12" r="8" fill="none" stroke="var(--brand-blue)" stroke-width="5"/></svg>
      <h2 class="topic-title">Subtext title here</h2>
      <p class="topic-body"><span>Subtext here Subtext here Subtext here Subtext here Subtext here Subtext here Subtext here Subtext here</span><span>Subtext here Subtext here Subtext here Subtext here Subtext here Subtext here</span></p>
    </li>
    <li class="topic">
      <svg class="topic-bullet" viewBox="0 0 24 24" aria-hidden="true"><circle cx="12" cy="12" r="8" fill="none" stroke="var(--brand-blue)" stroke-width="5"/></svg>
      <h2 class="topic-title">Subtext title here</h2>
      <p class="topic-body"><span>Subtext here Subtext here Subtext here Subtext here Subtext here Subtext here Subtext here Subtext here</span><span>Subtext here Subtext here Subtext here Subtext here Subtext here Subtext here</span></p>
    </li>
    <li class="topic">
      <svg class="topic-bullet" viewBox="0 0 24 24" aria-hidden="true"><circle cx="12" cy="12" r="8" fill="none" stroke="var(--brand-blue)" stroke-width="5"/></svg>
      <h2 class="topic-title">Subtext title here</h2>
      <p class="topic-body"><span>Subtext here Subtext here Subtext here Subtext here Subtext here Subtext here Subtext here Subtext here</span><span>Subtext here Subtext here Subtext here Subtext here Subtext here Subtext here</span></p>
    </li>
  </ul>
</main>
</body>
</html>
```